Long term design collaboration - mobile app design & web app design

We are looking for a talented mobile designer to help us improve our UI & UX for mobile app and web app.

The screens that need to be redesigned are attached.

There is potentially a lot more work in future design available for the successful candidate.
The successful candidate would have to take part in daily stand-up around 3 times per week.
The successful candidate would join a dev team
We are software company that does property management

```html
<!DOCTYPE html>
<html lang="en">
<head>
<meta charset="utf-8">
<title>Property Management App Screens</title>
<link href="https://fonts.googleapis.com/css2?family=Poppins:wght@500;600&family=Roboto:wght@400;500&display=swap" rel="stylesheet">
<style>
:root{
  --stage:#8c8c8c;
  --blue:#2a5bbf;
  --blue-dark:#234fa8;
  --ink:#1c1f26;
  --muted:#555b66;
  --grey:#9aa0aa;
  --card:#ffffff;
  --bg-top:#ffffff;
  --bg-bottom:#e3e9f6;
  --amber:#f2a516;
  --red:#e3261b;
}
*{box-sizing:border-box;margin:0;padding:0}
html,body{width:1200px;height:2596px;overflow:hidden;background:var(--stage)}
.board{position:absolute;left:0;top:0;width:1026px;height:2220px;transform:scale(1.16959);transform-origin:0 0}
.phone{position:absolute;width:375px;overflow:hidden;background:linear-gradient(180deg,var(--bg-top) 0%,var(--bg-bottom) 100%);font-family:Roboto,Arial,sans-serif;color:var(--ink)}
.header{position:absolute;left:0;top:0;width:375px;height:142px}
.time{position:absolute;left:30px;top:17px;color:#fff;font:500 13px/16px Roboto,sans-serif}
.status{position:absolute;right:30px;top:19px}
.back{position:absolute;left:22px;top:73px}
.menu{position:absolute;left:320px;top:65px;width:32px;height:32px;border-radius:50%;background:#fff;display:flex;align-items:center;justify-content:center}
.screen-title{position:absolute;left:60px;right:60px;color:#fff;text-align:center;font:600 22px/30px Poppins,sans-serif}
.sec-title{position:absolute;left:0;width:100%;text-align:center;font:500 23px/32px Poppins,sans-serif;color:var(--ink)}
.sec-title::after{content:"";position:absolute;left:50%;top:34px;width:56px;height:3px;margin-left:-28px;background:var(--blue);border-radius:2px}
.card{position:absolute;left:23px;width:330px;height:70px;background:var(--card);border-radius:8px;box-shadow:0 4px 14px rgba(40,70,140,.08)}
.card .label{position:absolute;left:17px;top:14px;font-size:15px;line-height:18px;color:var(--ink);display:flex;align-items:center;gap:4px}
.card .value{position:absolute;left:16px;top:35px;font-size:12px;line-height:15px;color:var(--muted)}
.card .chev{position:absolute;right:15px;top:21px}
.badge{display:inline-flex;width:13px;height:13px;border-radius:50%;color:#fff;font:700 10px/13px Roboto,sans-serif;justify-content:center}
.badge.warn{background:var(--amber)}
.badge.alert{background:var(--red)}
.fin-card{position:absolute;left:23px;width:330px;height:80px;background:var(--card);border-radius:8px;box-shadow:0 4px 14px rgba(40,70,140,.08)}
.fin-card.active{background:var(--blue);color:#fff}
.fin-card .label{position:absolute;left:13px;top:0;height:80px;display:flex;align-items:center;font-size:15px;line-height:23px}
.fin-card .divider{position:absolute;top:14px;width:1px;height:52px;background:#e4e7ee}
.fin-card.active .divider{background:rgba(255,255,255,.25)}
.fin-card .col{position:absolute;top:15px;width:80px;margin-left:-40px;text-align:center}
.fin-card .amount{font:500 12px/16px Roboto,sans-serif;color:var(--ink);margin-top:3px}
.fin-card .caption{font-size:12px;line-height:16px;color:var(--grey);margin-top:3px}
.fin-card.active .amount,.fin-card.active .caption{color:#fff}
.fin-card .go{position:absolute;left:285px;top:25px;width:30px;height:30px;border-radius:50%;background:var(--blue);display:flex;align-items:center;justify-content:center}
.fin-card.active .go{background:#fff}
.option{position:absolute;left:23px;width:330px;height:70px;background:var(--card);border-radius:8px;box-shadow:0 4px 14px rgba(40,70,140,.08);display:flex;align-items:center}
.option .box{position:absolute;left:23px;top:28px}
.option .text{position:absolute;left:56px;right:40px;font-size:15px;line-height:21px;color:var(--ink)}
.btn{position:absolute;top:523px;width:130px;height:48px;border-radius:8px;font:500 16px/48px Roboto,sans-serif;text-align:center;letter-spacing:.2px}
.btn.ghost{left:54px;border:1.5px solid var(--blue);color:var(--blue);background:#fff}
.btn.primary{left:192px;background:var(--blue);color:#fff;box-shadow:0 4px 10px rgba(42,91,191,.3)}
.nav{position:absolute;left:23px;width:330px;height:55px;border:1.5px solid var(--blue);border-top:none;border-radius:0 0 8px 8px}
.nav::before{content:"";position:absolute;left:-1.5px;right:-1.5px;top:0;height:8px;border:1.5px solid var(--blue);border-bottom:none;border-radius:8px 8px 0 0}
.nav-item{position:absolute;top:-21px;width:82px;margin-left:-41px;text-align:center;font-size:13px;line-height:16px;color:var(--ink)}
.nav-item .ic{width:42px;height:42px;margin:0 auto 12px;border-radius:50%;background:#fff;border:1.5px solid var(--blue);display:flex;align-items:center;justify-content:center;color:var(--blue)}
.nav-item.current .ic{background:var(--blue);color:#fff}
</style>
</head>
<body>
<svg width="0" height="0" style="position:absolute">
  <defs>
    <symbol id="i-chev" viewBox="0 0 30 30"><circle cx="15" cy="15" r="14" fill="#fff" stroke="#2a5bbf" stroke-width="1.4"/><path d="M13 10l5 5-5 5" fill="none" stroke="#2a5bbf" stroke-width="1.6" stroke-linecap="round" stroke-linejoin="round"/></symbol>
    <symbol id="i-home" viewBox="0 0 20 20"><path d="M10 3L2 10h2.5v7h4v-4.5h3V17h4v-7H18z" fill="currentColor"/></symbol>
    <symbol id="i-search" viewBox="0 0 20 20"><circle cx="8.5" cy="8.5" r="5.5" fill="none" stroke="currentColor" stroke-width="2.4"/><path d="M12.5 12.5L17 17" stroke="currentColor" stroke-width="2.8" stroke-linecap="round"/></symbol>
    <symbol id="i-chart" viewBox="0 0 20 20"><path d="M3 3v14h14" fill="none" stroke="currentColor" stroke-width="1.8"/><rect x="6" y="9" width="2" height="6" fill="currentColor"/><rect x="9.5" y="6" width="2" height="9" fill="currentColor"/><rect x="13" y="10" width="2" height="5" fill="currentColor"/></symbol>
    <symbol id="i-chat" viewBox="0 0 20 20"><ellipse cx="8" cy="8" rx="6.5" ry="4.8" fill="currentColor"/><path d="M4 11.5L3 15l4-2.5z" fill="currentColor"/><ellipse cx="13" cy="11.5" rx="5.5" ry="4" fill="currentColor" stroke="#fff" stroke-width="1"/><path d="M16 14.5l1.5 3-3.5-2z" fill="currentColor"/></symbol>
    <symbol id="i-doc" viewBox="0 0 10 12"><path d="M0 1a1 1 0 011-1h5l4 4v7a1 1 0 01-1 1H1a1 1 0 01-1-1z" fill="currentColor"/><path d="M2.5 6.5h5M2.5 8.5h5" stroke="#fff" stroke-width=".9"/></symbol>
    <symbol id="i-status" viewBox="0 0 58 12"><rect x="0" y="8" width="2.5" height="3" fill="#fff"/><rect x="4" y="6" width="2.5" height="5" fill="#fff"/><rect x="8" y="4" width="2.5" height="7" fill="#fff"/><rect x="12" y="2" width="2.5" height="9" fill="#fff"/><path d="M19 5a8 8 0 0112 0M21.5 7.5a4.5 4.5 0 017 0" fill="none" stroke="#fff" stroke-width="1.6"/><circle cx="25" cy="10" r="1.3" fill="#fff"/><rect x="36" y="1.5" width="19" height="9" rx="2.5" fill="none" stroke="#fff" stroke-width="1"/><rect x="38" y="3.5" width="15" height="5" rx="1" fill="#fff"/><rect x="56" y="4.5" width="1.5" height="3" fill="#fff"/></symbol>
    <symbol id="i-back" viewBox="0 0 24 14"><path d="M23 7H3M8 2L2 7l6 5" fill="none" stroke="#fff" stroke-width="2.4" stroke-linecap="round" stroke-linejoin="round"/></symbol>
    <symbol id="i-menu" viewBox="0 0 14 12"><path d="M1 1.5h12M1 6h12M1 10.5h12" stroke="#1c1f26" stroke-width="2.2" stroke-linecap="round"/></symbol>
  </defs>
</svg>

<main class="board">

  <!-- Development overview screen -->
  <section class="phone" style="left:98px;top:119px;height:1982px">
    <svg class="header" viewBox="0 0 375 142"><path d="M0 0H375V92Q187.5 192 0 92Z" fill="var(--blue)"/></svg>
    <div class="time">12:00 ➚</div>
    <svg class="status" width="58" height="12"><use href="#i-status"/></svg>
    <svg class="back" width="24" height="14"><use href="#i-back"/></svg>
    <h1 class="screen-title" style="top:58px">Development Overview</h1>
    <div class="menu"><svg width="14" height="12"><use href="#i-menu"/></svg></div>

    <h2 class="sec-title" style="top:179px">Overview</h2>
    <div class="card" style="top:239px"><div class="label">Units</div><div class="value">85</div><svg class="chev" width="30" height="30"><use href="#i-chev"/></svg></div>
    <div class="card" style="top:320px"><div class="label">Handover date</div><div class="value">12 January 2023</div><svg class="chev" width="30" height="30"><use href="#i-chev"/></svg></div>
    <div class="card" style="top:402px"><div class="label">Address</div><div class="value">24 Elmstead Crescent, London, N4 2QR</div><svg class="chev" width="30" height="30"><use href="#i-chev"/></svg></div>
    <div class="card" style="top:483px"><div class="label">Section 20 limit</div><div class="value">£20</div><svg class="chev" width="30" height="30"><use href="#i-chev"/></svg></div>

    <h2 class="sec-title" style="top:606px">Compliance</h2>
    <div class="card" style="top:667px"><div class="label">Asbestos</div><div class="value">NA</div><svg class="chev" width="30" height="30"><use href="#i-chev"/></svg></div>
    <div class="card" style="top:748px"><div class="label">Legionellas <span class="badge warn">?</span></div><div class="value">-</div><svg class="chev" width="30" height="30"><use href="#i-chev"/></svg></div>
    <div class="card" style="top:829px"><div class="label">Drains <span class="badge alert">i</span></div><div class="value">Overdue, 10 December 2023</div><svg class="chev" width="30" height="30"><use href="#i-chev"/></svg></div>
    <div class="card" style="top:911px"><div class="label">Gutters</div><div class="value">NA</div><svg class="chev" width="30" height="30"><use href="#i-chev"/></svg></div>
    <div class="card" style="top:991px"><div class="label">Dry Risers</div><div class="value">NA</div><svg class="chev" width="30" height="30"><use href="#i-chev"/></svg></div>

    <h2 class="sec-title" style="top:1110px">Insurances</h2>
    <div class="card" style="top:1171px"><div class="label">Terrorism</div><div class="value">NA</div><svg class="chev" width="30" height="30"><use href="#i-chev"/></svg></div>
    <div class="card" style="top:1252px"><div class="label">Buildings</div><div class="value">NA</div><svg class="chev" width="30" height="30"><use href="#i-chev"/></svg></div>
    <div class="card" style="top:1334px"><div class="label">Engineering</div><div class="value">NA</div><svg class="chev" width="30" height="30"><use href="#i-chev"/></svg></div>
    <div class="card" style="top:1415px"><div class="label">D&amp;O</div><div class="value">NA</div><svg class="chev" width="30" height="30"><use href="#i-chev"/></svg></div>
    <div class="card" style="top:1495px"><div class="label">Reinstatemen</div><div class="value">NA</div><svg class="chev" width="30" height="30"><use href="#i-chev"/></svg></div>

    <h2 class="sec-title" style="top:1619px">Service Charge</h2>
    <div class="card" style="top:1679px"><div class="label">Year End</div><div class="value">12/12/2024</div><svg class="chev" width="30" height="30"><use href="#i-chev"/></svg></div>
    <div class="card" style="top:1760px"><div class="label">Demand Dates</div><div class="value">NA</div><svg class="chev" width="30" height="30"><use href="#i-chev"/></svg></div>

    <nav class="nav" style="top:1903px">
      <div class="nav-item current" style="left:42px"><div class="ic"><svg width="20" height="20"><use href="#i-home"/></svg></div>Home</div>
      <div class="nav-item" style="left:124px"><div class="ic"><svg width="20" height="20"><use href="#i-search"/></svg></div>Overview</div>
      <div class="nav-item" style="left:205px"><div class="ic"><svg width="20" height="20"><use href="#i-chart"/></svg></div>Finances</div>
      <div class="nav-item" style="left:287px"><div class="ic"><svg width="20" height="20"><use href="#i-chat"/></svg></div>Messages</div>
    </nav>
  </section>

  <!-- Finances screen -->
  <section class="phone" style="left:554px;top:119px;height:812px">
    <svg class="header" viewBox="0 0 375 142"><path d="M0 0H375V92Q187.5 192 0 92Z" fill="var(--blue)"/></svg>
    <div class="time">12:00 ➚</div>
    <svg class="status" width="58" height="12"><use href="#i-status"/></svg>
    <svg class="back" width="24" height="14" style="top:74px"><use href="#i-back"/></svg>
    <h1 class="screen-title" style="top:74px">Finances</h1>
    <div class="menu"><svg width="14" height="12"><use href="#i-menu"/></svg></div>

    <h2 class="sec-title" style="top:179px">Accounts Receivable</h2>
    <div class="fin-card" style="top:239px">
      <div class="label">Arrears</div>
      <div class="divider" style="left:109px"></div><div class="divider" style="left:194px"></div>
      <div class="col" style="left:151px;color:var(--blue)"><svg width="10" height="12"><use href="#i-doc"/></svg><div class="amount">£7,268.22</div><div class="caption">Total</div></div>
      <div class="col" style="left:233px;color:var(--blue)"><svg width="10" height="12"><use href="#i-doc"/></svg><div class="amount">5</div><div class="caption">Receipts</div></div>
      <div class="go"><svg width="12" height="12" viewBox="0 0 12 12"><path d="M4 2l4 4-4 4" fill="none" stroke="#fff" stroke-width="1.8" stroke-linecap="round" stroke-linejoin="round"/></svg></div>
    </div>
    <div class="fin-card active" style="top:333px">
      <div class="label">Unallocated<br>Receipts</div>
      <div class="divider" style="left:109px"></div><div class="divider" style="left:194px"></div>
      <div class="col" style="left:151px;color:#fff"><svg width="10" height="12"><use href="#i-doc"/></svg><div class="amount">£7,268.22</div><div class="caption">Total</div></div>
      <div class="col" style="left:233px;color:#fff"><svg width="10" height="12"><use href="#i-doc"/></svg><div class="amount">5</div><div class="caption">Receipts</div></div>
      <div class="go"><svg width="12" height="12" viewBox="0 0 12 12"><path d="M4 2l4 4-4 4" fill="none" stroke="#1c1f26" stroke-width="1.8" stroke-linecap="round" stroke-linejoin="round"/></svg></div>
    </div>

    <h2 class="sec-title" style="top:456px">Accounts Payable</h2>
    <div class="fin-card" style="top:516px">
      <div class="label">Invoices</div>
      <div class="divider" style="left:109px"></div><div class="divider" style="left:194px"></div>
      <div class="col" style="left:151px;color:var(--blue)"><svg width="10" height="12"><use href="#i-doc"/></svg><div class="amount">£4,268.78</div><div class="caption">Total</div></div>
      <div class="col" style="left:233px;color:var(--blue)"><svg width="10" height="12"><use href="#i-doc"/></svg><div class="amount">5</div><div class="caption">Receipts</div></div>
      <div class="go"><svg width="12" height="12" viewBox="0 0 12 12"><path d="M4 2l4 4-4 4" fill="none" stroke="#fff" stroke-width="1.8" stroke-linecap="round" stroke-linejoin="round"/></svg></div>
    </div>

    <nav class="nav" style="top:740px">
      <div class="nav-item" style="left:42px"><div class="ic"><svg width="20" height="20"><use href="#i-home"/></svg></div>Home</div>
      <div class="nav-item" style="left:124px"><div class="ic"><svg width="20" height="20"><use href="#i-search"/></svg></div>Overview</div>
      <div class="nav-item current" style="left:205px"><div class="ic"><svg width="20" height="20"><use href="#i-chart"/></svg></div>Finances</div>
      <div class="nav-item" style="left:287px"><div class="ic"><svg width="20" height="20"><use href="#i-chat"/></svg></div>Messages</div>
    </nav>
  </section>

  <!-- Legionellas screen -->
  <section class="phone" style="left:554px;top:1005px;height:812px">
    <svg class="header" viewBox="0 0 375 142"><path d="M0 0H375V92Q187.5 192 0 92Z" fill="var(--blue)"/></svg>
    <div class="time">12:00 ➚</div>
    <svg class="status" width="58" height="12"><use href="#i-status"/></svg>
    <svg class="back" width="24" height="14"><use href="#i-back"/></svg>
    <h1 class="screen-title" style="top:74px">Legionellas</h1>
    <div class="menu"><svg width="14" height="12"><use href="#i-menu"/></svg></div>

    <h2 class="sec-title" style="top:179px">Is it required?</h2>
    <div class="option" style="top:239px">
      <svg class="box" width="15" height="15"><rect x=".75" y=".75" width="13.5" height="13.5" rx="2" fill="#fff" stroke="#9aa0aa" stroke-width="1.3"/></svg>
      <div class="text">No</div>
    </div>
    <div class="option" style="top:320px">
      <svg class="box" width="15" height="15"><rect x=".75" y=".75" width="13.5" height="13.5" rx="2" fill="#fff" stroke="#9aa0aa" stroke-width="1.3"/></svg>
      <div class="text">Yes, but I do not have a file to upload</div>
    </div>
    <div class="option" style="top:400px">
      <svg class="box" width="18" height="16" viewBox="0 0 18 16"><rect x=".75" y="1.75" width="13.5" height="13.5" rx="2" fill="#fff" stroke="var(--blue)" stroke-width="1.3"/><path d="M3.5 8l3.5 3.5L16.5 1.5" fill="none" stroke="var(--blue)" stroke-width="2" stroke-linecap="round"/></svg>
      <div class="text">Yes, and I have a file to upload</div>
    </div>

    <div class="btn ghost">BACK</div>
    <div class="btn primary">NEXT ›</div>

    <nav class="nav" style="top:740px">
      <div class="nav-item" style="left:42px"><div class="ic"><svg width="20" height="20"><use href="#i-home"/></svg></div>Home</div>
      <div class="nav-item" style="left:124px"><div class="ic"><svg width="20" height="20"><use href="#i-search"/></svg></div>Overview</div>
      <div class="nav-item current" style="left:205px"><div class="ic"><svg width="20" height="20"><use href="#i-chart"/></svg></div>Finances</div>
      <div class="nav-item" style="left:287px"><div class="ic"><svg width="20" height="20"><use href="#i-chat"/></svg></div>Messages</div>
    </nav>
  </section>

</main>
</body>
</html>
```